Vosh CBD Pod package and logo design.

Vosh is the brand name for our line of CBD Plim style pods. I would like the logo to be designed as well as the packaging. The packaging will be the same size as the Plim pod packaging. I would also like the box to be white and have a similar clean look just as Plim does. My vision for the brand is very simple with black letters in a font similar to the picture attached. I would also like an animated marijuana flower that is extremely simple and also very similar to the picture attached below. Please note that I do not want the logo to be an exact copy of the example attached. I have also attached a picture of the Plim packaging.

Although I do like my idea of the logo I am very much open to your creative ideas and will absolutely consider any other logo designs outside of my description. One final note, outside of the simple marijuana flower above the "i", I do not want the logo to scream "Marijuana" as it is a CBD product and the overt marijuana referenced brands dont fair to well to the non-marijuana user. If you have any questions, please do not hesitate to ask.

```html
<!DOCTYPE html>
<html lang="en">
<head>
<meta charset="utf-8">
<title>Vosh Mango Pods Package</title>
<link rel="stylesheet" href="https://fonts.googleapis.com/css2?family=Dosis:wght@300;400&family=Arimo:wght@700&display=swap">
<style>
  :root {
    --backdrop: #f1f1f1;
    --box-white: #ffffff;
    --ink: #2b2b2b;
    --lime: #a6cf3c;
    --mango: #f5924d;
    --mango-light: #f9a566;
    --pod-dark: #1c1c1c;
    --pod-mid: #3a3a3a;
    --warning-ink: #6a6a6a;
    --warning-frame: #7c7c7c;
    --label-grey: #555555;
  }
  * { margin: 0; padding: 0; box-sizing: border-box; }
  html, body {
    width: 1200px;
    height: 1002px;
    overflow: hidden;
    background: var(--backdrop);
  }
  .package-front {
    position: absolute;
    left: 381px;
    top: 146px;
    width: 438px;
    height: 710px;
    background: var(--box-white);
  }
  .brand-name {
    position: absolute;
    left: 112px;
    top: 112px;
    font-family: "Dosis", sans-serif;
    font-weight: 300;
    font-size: 86px;
    line-height: 1;
    color: var(--ink);
    letter-spacing: 1px;
  }
  .strength-badge {
    position: absolute;
    left: 306px;
    top: 134px;
    width: 90px;
    height: 90px;
    border-radius: 50%;
    background: var(--lime);
    color: var(--box-white);
    font-family: "Dosis", sans-serif;
    font-weight: 400;
    font-size: 52px;
    display: flex;
    align-items: center;
    justify-content: center;
  }
  .pod-row {
    position: absolute;
    left: 46px;
    top: 252px;
    width: 352px;
    height: 148px;
    display: flex;
    justify-content: space-between;
  }
  .pod {
    width: 72px;
    height: 148px;
    background: linear-gradient(to bottom,
      var(--mango-light) 0%, var(--mango) 46%,
      var(--pod-mid) 46%, var(--pod-dark) 100%);
  }
  .flavour-line {
    position: absolute;
    left: 0;
    width: 100%;
    top: 412px;
    text-align: center;
    font-family: "Dosis", sans-serif;
    font-weight: 300;
    font-size: 24px;
    color: var(--label-grey);
  }
  .flavour-name {
    font-size: 34px;
    color: var(--mango);
  }
  .nicotine-warning {
    position: absolute;
    left: 20px;
    top: 466px;
    width: 402px;
    height: 232px;
    border: 4px solid var(--warning-frame);
    background: var(--box-white);
    display: flex;
    align-items: center;
    justify-content: center;
    text-align: center;
    font-family: "Arimo", sans-serif;
    font-weight: 700;
    font-size: 29px;
    line-height: 1.28;
    color: var(--warning-ink);
  }
</style>
</head>
<body>
  <main class="package-front">
    <div class="brand-name">Vosh</div>
    <div class="strength-badge">5%</div>

    <div class="pod-row" role="img" aria-label="Four mango pods, orange tops with black bases">
      <div class="pod"></div>
      <div class="pod"></div>
      <div class="pod"></div>
      <div class="pod"></div>
    </div>

    <p class="flavour-line"><span class="flavour-name">MANGO</span> - 4 Pods</p>

    <div class="nicotine-warning">
      <p>WARNING:<br>This product contains<br>nicotine. Nicotine is an<br>addictive chemical.</p>
    </div>
  </main>
</body>
</html>
```